Letterhead Design for Corvinta Communications

We are a Telecommunications Company, We wanting to get our Letterhead sorted as the one we have now looks Dull, It be used across our different databases we use but also mainly in Word , I have attached our Logo for you also, our website is corvinta-example.com.au

We would only like to show our postal Address which is PO Box 8146 Kelso Reach NSW 2984

and we need to show our ABN Number Which we would be ABN: 71 408 236 914

Target Market(s)

Looks Stunning for our Proposals and General Usage

Industry/Entity Type

Telecommunications

Requirements
Must have
• Our Postal Address Only and Our ABN Number
Should not have
• Not listing our Actual Address

```html
<!DOCTYPE html>
<html lang="en">
<head>
<meta charset="utf-8">
<title>Corvinta Communications Letterhead</title>
<link rel="stylesheet" href="https://fonts.googleapis.com/css2?family=Arimo:wght@400;700&family=Montserrat:wght@600;700&display=swap">
<style>
  :root {
    --backdrop: #e8e8e8;
    --paper: #e6e6e6;
    --ink: #4a4a4a;
    --brand-orange: #d4561c;
    --brand-green: #19a51c;
    --rule-grey: #6a6a6a;
    --watermark: #dcdcdc;
    --signature-tone: #cfcfcf;
  }
  * { margin: 0; padding: 0; box-sizing: border-box; }
  html, body { width: 1200px; height: 1024px; overflow: hidden; background: var(--backdrop); }
  .letterhead {
    position: absolute; left: 252px; top: 20px;
    width: 696px; height: 984px;
    background: var(--paper);
    overflow: hidden;
    box-shadow: 0 6px 24px rgba(0,0,0,0.12);
    font-family: "Arimo", Arial, sans-serif;
    color: var(--ink);
  }
  .watermark-circle {
    position: absolute; left: 303px; top: 590px;
    width: 400px; height: 400px; border-radius: 50%;
    background: var(--watermark);
  }
  .band-green {
    position: absolute; left: 0; right: 0; top: 93px; height: 5px;
    background: var(--brand-green);
  }
  .rule-grey {
    position: absolute; left: 0; right: 0; top: 103px; height: 1.5px;
    background: var(--rule-grey);
  }
  .brand {
    position: absolute; left: 42px; top: 50px;
    display: flex; align-items: center; gap: 10px;
    background: var(--paper); padding-right: 6px;
  }
  .brand-dot {
    width: 58px; height: 58px; border-radius: 50%;
    background: var(--brand-orange);
  }
  .brand-name {
    font-family: "Arimo", Arial, sans-serif;
    font-weight: 700; font-size: 16px; letter-spacing: 0.4px;
    color: var(--brand-orange); white-space: nowrap;
  }
  .contact {
    position: absolute; top: 45px;
    font-size: 12px; line-height: 14.4px;
    white-space: nowrap; font-style: normal;
  }
  .contact-address { right: 244px; text-align: right; }
  .contact-divider {
    position: absolute; left: 468px; top: 47px; width: 1.5px; height: 42px;
    background: var(--ink);
  }
  .contact-channels { left: 485px; }
  .contact-channels li { list-style: none; display: flex; align-items: center; gap: 7px; height: 14.4px; }
  .contact-channels svg { width: 10px; height: 10px; flex: none; }
  .letter {
    position: absolute; left: 63px; top: 303px; width: 572px;
  }
  .greeting {
    font-family: "Montserrat", sans-serif; font-weight: 600;
    font-size: 16px; margin-bottom: 30px;
  }
  .letter p.body {
    font-size: 12.2px; line-height: 14.4px; margin-bottom: 12px;
  }
  .closing {
    font-family: "Montserrat", sans-serif; font-weight: 700;
    font-size: 9.5px; margin-top: 24px;
  }
  .signature {
    margin-top: 24px; width: 116px; height: 34px; border-radius: 4px;
    background: var(--signature-tone);
  }
</style>
</head>
<body>
  <main class="letterhead">
    <div class="watermark-circle" aria-hidden="true"></div>

    <header class="letter-header">
      <div class="band-green"></div>
      <div class="rule-grey"></div>
      <div class="brand">
        <span class="brand-dot" aria-hidden="true"></span>
        <span class="brand-name">Corvinta Communications</span>
      </div>

      <address class="contact contact-address">
        PO Box 8146<br>Kelso Reach NSW 2984<br>ABN: 71 408 236 914
      </address>
      <div class="contact-divider"></div>
      <ul class="contact contact-channels">
        <li>
          <svg viewBox="0 0 10 10" aria-hidden="true"><path d="M2 1 L4 3 L3 4.3 Q4.2 6 5.7 7 L7 6 L9 8 L7.8 9.3 Q4 9 0.8 3.2 Z" fill="#d4561c"/></svg>
          1800 614 072
        </li>
        <li>
          <svg viewBox="0 0 10 10" aria-hidden="true"><rect x="0.5" y="2" width="9" height="6.5" fill="#d4561c"/><path d="M0.5 2 L5 5.5 L9.5 2" fill="none" stroke="#e6e6e6" stroke-width="0.9"/></svg>
          info@corvinta-example.com.au
        </li>
        <li>
          <svg viewBox="0 0 10 10" aria-hidden="true"><circle cx="5" cy="5" r="4.5" fill="#d4561c"/><path d="M0.5 5 H9.5 M5 0.5 Q2.5 5 5 9.5 M5 0.5 Q7.5 5 5 9.5" fill="none" stroke="#e6e6e6" stroke-width="0.7"/></svg>
          www.corvinta-example.com.au
        </li>
      </ul>
    </header>

    <section class="letter">
      <h1 class="greeting">Dear Mr. Harlow,</h1>
      <p class="body">Lorem ipsum dolor sit amet, consectetuer adipiscing elit, sed diam nonmmy nibh euismod tincidunt ut laor eet dolore magna aliquam erat volutpat. Ut wisi enim ad minim veniam, quis nostrud exerci tationmcorper suscipit lobortis nisl ut aliquip ex ea commodo consequat. Duis autem vel eum iriure dolor in hendrerit in vulputate velit esse molestie consequat, vel illum dolore eu feugiat</p>
      <p class="body">Rorem ipsum dolor sit amet, consectetuer adipiscing elit, sed diam nonmmy nibh euismod tincidunt ut laor eet dolore magna aliquam erat volutpat. Ut wisi enim ad minim veniam, quis nostrud exerci tationmcorper suscipit lobortis nisl ut aliquip ex ea commodo consequat. Duis autem vel eum iriure dolor in hendrerit in vulputate velit esse molest</p>
      <p class="body">Dorem ipsum dolor sit amet, consectetuer adipiscing elit, sed diam nonmmy nibh euismod tincidunt ut laor eet dolore magna aliquam erat volutpat. Ut wisi enim ad minim veniam, quis nostrud exerci tationmcorper suscipit lobortis nisl ut aliquip ex ea commodo consequat. Duis autem vel eum iriure dolor in hendrerit in suscipit lobortis nisl ut aliquip ex ea commodo consequat. Duis autem vel eum iriure dolor in hendrerit in vulputate velit esse molestie consequat, vel illum</p>
      <p class="body">Sorem ipsum dolor sit amet, consectetuer adipiscing elit, sed diam nonmmy nibh euismod tincidunt ut laor eet dolore magna aliquam erat volutpat. Ut wisi enim ad minim veniam, quis nostrud exerci tationmcorper suscipit lobortis nisl ut aliquip ex ea commodo consequat. Duis autem vel eum iriure dolor in</p>
      <p class="closing">Sincerely,</p>
      <div class="signature" role="img" aria-label="Handwritten signature of the sender"></div>
    </section>
  </main>
</body>
</html>
```